Zielgruppe
Wir sind KQ Rapid Voltwerk GmbH mit Sitz in Basel Schweiz. Wir bieten die volle Palette von Elektronikdienstleistungen. Besonders aber Photovoltaik (Solar) auf Einfamilienhäusern und Gewerbeeinheiten, Smart Home Automation mit Dravix (Partner) und allgemeine Elektrikerdienstleistungen in Häusern und Wohnung.
USP
• Regionale Firma, BS, BL,AG
○ Daher schnelle Reaktion im Störungsfall. Garantierte Entstörung
• Umsetzung innert 2-3 Monate
• Planung und Durchführung aus einer Hand.
• Umsetzung auch in der PV Installation nur durch eigene Mitarbeiter
• Kelmora Förderung, bis zu 6TCHF
• Kompetent, freundlich
• Eidgenössich diplomierter Elektroinstallateur (Meister)
• EFZ (Eidgenösisch Fährigkeitszeugnis)
• 1 Jahr Existenz
• Dravix goldpartner
• Nur Doppelglasmodule mit 25 Jahre Garantie, 10 Jahre auf Wechselrichter und Batterie
• Planung mittels CAD/*D Planung, technische Tool
• Genaues und schnelles Angebot innert 5 Werktagen
USP:
• Stromkosten sparen
• Autark werden, unabhängig von Strompreisentwicklung
• Umwelt schützen
WUNSCHKUNDE
• Soziodemografisch
○ Eigentümer
○ Gehobene Mittelklasse
• Lokalität in Basel und Umgebung
Aufgabenstellung
Medien unter: https://files.trobelix.ch/index.php/s/mQzWnLpRtYvA7KD
Logo ist dort vorhanden.
Hintergrund hell (weiss, hellgrau bspw.)
Schriftart
Verlinkungen zu Social Media:
• Facebook
• Linkedin
• Instagram
Beispielseiten, die gefallen:
Alpin Lichtfeld Werk (alpin-lichtfeld-werk.ch) Prio
Counter mit

```html
<!DOCTYPE html>
<html lang="de">
<head>
<meta charset="utf-8">
<title>KQ Rapid Voltwerk GmbH – Engagement</title>
<link href="https://fonts.googleapis.com/css2?family=Hind:wght@400;500;600&family=Montserrat:wght@600;700&display=swap" rel="stylesheet">
<style>
  :root {
    --bg-top: #f4f4f4;
    --bg-mid: #ececec;
    --green: #3e7d2a;
    --green-soft: #5e9d47;
    --heading: #7d8ea0;
    --text: #2f2f2f;
    --red: #d4252c;
    --white: #ffffff;
  }
  * { margin: 0; padding: 0; box-sizing: border-box; }
  html, body { width: 1200px; height: 889px; overflow: hidden; }
  body {
    position: relative;
    font-family: "Hind", sans-serif;
    color: var(--text);
    background: linear-gradient(180deg, var(--bg-top) 0%, var(--bg-mid) 62%, #c9dcc0 78%, var(--green-soft) 100%);
  }
  .section-title {
    position: absolute;
    top: -34px;
    left: 0;
    width: 1060px;
    text-align: center;
    font-family: "Montserrat", sans-serif;
    font-weight: 700;
    font-size: 54px;
    color: var(--heading);
  }
  .portrait {
    position: absolute;
    left: 72px;
    top: 92px;
    width: 330px;
    height: 345px;
    border-radius: 50%;
    background: radial-gradient(circle at 70% 40%, #c9c9c4 0%, #8d8f8a 45%, #2c2c2c 100%);
  }
  .about-text {
    position: absolute;
    left: 440px;
    top: 100px;
    width: 650px;
    font-size: 19px;
    line-height: 24px;
  }
  .about-text p { margin-bottom: 22px; }
  .btn {
    position: absolute;
    display: flex;
    align-items: center;
    justify-content: center;
    color: var(--white);
    text-decoration: none;
    border-radius: 3px;
    box-shadow: 0 3px 6px rgba(0,0,0,0.25);
  }
  .btn-services {
    left: 440px;
    top: 438px;
    width: 362px;
    height: 58px;
    background: var(--green);
    font-family: "Hind", sans-serif;
    font-weight: 600;
    font-size: 25px;
  }
  .team-photo {
    position: absolute;
    left: 150px;
    top: 620px;
    width: 690px;
    height: 269px;
    background: linear-gradient(180deg, #e9ece9 0%, #cfd3d1 55%, #4b4b4b 100%);
  }
  .btn-contact {
    left: 1038px;
    top: 806px;
    width: 152px;
    height: 56px;
    background: var(--red);
    font-family: "Montserrat", sans-serif;
    font-weight: 600;
    font-size: 24px;
  }
</style>
</head>
<body>
  <h2 class="section-title">Engagement</h2>

  <div class="portrait" role="img" aria-label="Porträt eines Elektroinstallateurs mit Laptop vor einem Verteilerschrank"></div>

  <div class="about-text">
    <p>Seit unserer Gründung haben wir uns zu einem etablierten Unternehmen entwickelt, das stolz auf seine regionale Verwurzelung und die Zufriedenheit unserer Kunden ist. Unsere kontinuierliche Weiterentwicklung spiegelt unser Engagement für Exzellenz und Kundenzufriedenheit wider.</p>
    <p>Unsere erfahrenen Fachleute, angeführt von einem eidgenössisch diplomierten Elektroinstallateur (Meister), stehen Ihnen mit ihrem Fachwissen und ihrer Leidenschaft zur Verfügung. Als Team setzen wir uns tagtäglich dafür ein, Elektroniklösungen zu schaffen, die Ihre Erwartungen übertreffen.</p>
    <p>Unsere Mission ist es, innovative Elektroniklösungen anzubieten, die nicht nur höchsten Qualitätsstandards entsprechen, sondern auch zu nachhaltigem Wachstum und Umweltschutz beitragen. Wir leben Werte wie Integrität, Kundenzufriedenheit und Umweltbewusstsein in jedem Schritt unserer Arbeit.</p>
  </div>

  <a class="btn btn-services" href="#dienstleistungen">Zu unseren Dienstleistungen</a>

  <div class="team-photo" role="img" aria-label="Teamfoto der Mitarbeitenden vor dem weissen Firmenlieferwagen"></div>

  <a class="btn btn-contact" href="#kontakt">Kontakt</a>
</body>
</html>
```